wardrobe/costume stylist needs good business card for own business

Hi:)

I'm wanting a business card for my company. I am a freelance stylist.

I do wardrobe/costume stylist to TV commercials; Films; Fashion and Lifestyle shoots.

I'd like a design based around my name Rosalind Pember written nicely, maybe a colour? Up to you?!

I've attached a couple of images of business cards I like
.... be creative and have fun!

Thank you :)
Updates

Reason: I was trying to get my new business card ready for before I headed overseas Friday morning but I don't think that was realistic so I'd like to extend the deadline to give time to the project. Thank you

Hi designers:) Thank you for all your designs, I've extended the deadline until Sunday, so there's a bit more time. I've attached 3 pictures of business cards which I quite like, please take a look to see if it can be of help in your process. I like the pale plain or patterned background with dark font and the dark plain or patterned background with the pale font the motifs the feminine fonts the plain fonts I like the idea of playing with a circle or some shape on one side of the card with my name or initials as in the picture I have on my post could you play around with this idea a bit please? Thank you all for the work you've done :) Rosa

Hi I am working overseas til Saturday night sorry for no feedback until I teturn Thanks :) Rosa

Hi designers, Thank you all so much for submitting your designs, I really appreciate your input into my project :) I'm sorry I didn't get to respond to some comments, and give feedback. I didn't back from being away until later than I expected, and the deadline had passed then, so apologies. Thanks to you all again for all your really good designs :) Rosa

Target Market(s)

I am a freelance stylist my target audience is producers, production companies, photographers, directors...

Industry/Entity Type

Business

Requirements
Must have
• Rosalind Pember
Stylist or Wardrobe Stylist

email rosapember@quillnet.co.nz
Mobile 0218846193

(Don't have to use the words 'email' and 'mobile')
Nice to have
• Would like it to be double sided
Like B & W
Like pale colour background with dark font or white font
Like dark colour background with pale font
Should not have
• I would prefer it not to incorporate pictures

```html
<!DOCTYPE html>
<html lang="en">
<head>
<meta charset="utf-8">
<title>Rosalind Pember — Business Card</title>
<link href="https://fonts.googleapis.com/css2?family=Bodoni+Moda:wght@400&family=Cormorant+Garamond:wght@400&family=Open+Sans:wght@300&display=swap" rel="stylesheet">
<style>
  :root {
    --stage: #2b2b2b;
    --card-light: #ffffff;
    --card-dark: #000000;
    --bronze: #9b7a5c;
    --rule: #6f6f6f;
    --muted: #a08466;
  }
  * { margin: 0; padding: 0; box-sizing: border-box; }
  html, body {
    width: 1200px;
    height: 655px;
    overflow: hidden;
    background: var(--stage);
  }
  .canvas {
    position: relative;
    width: 1200px;
    height: 655px;
  }
  .card-face {
    position: absolute;
    top: 213px;
    width: 393px;
    height: 229px;
  }
  .card-front {
    left: 207px;
    background: var(--card-light);
  }
  .card-back {
    left: 600px;
    background: var(--card-dark);
  }
  .monogram-disc {
    position: absolute;
    left: 120px;
    top: 37px;
    width: 154px;
    height: 154px;
    border-radius: 50%;
    background: var(--bronze);
    display: flex;
    align-items: center;
    justify-content: center;
  }
  .monogram-name {
    font-family: "Bodoni Moda", serif;
    font-weight: 400;
    font-size: 17px;
    line-height: 1.15;
    color: var(--card-light);
    text-align: center;
  }
  .holder-name {
    position: absolute;
    top: 92px;
    left: 0;
    width: 100%;
    text-align: center;
    font-family: "Bodoni Moda", serif;
    font-weight: 400;
    font-size: 40px;
    letter-spacing: 1px;
    color: var(--bronze);
  }
  .role-line {
    position: absolute;
    top: 182px;
    left: 50px;
    width: 295px;
    display: flex;
    align-items: center;
    gap: 6px;
  }
  .role-line .rule {
    flex: 1;
    height: 1px;
    background: var(--rule);
  }
  .role-title {
    font-family: "Cormorant Garamond", serif;
    font-size: 10.5px;
    letter-spacing: 0.6px;
    color: var(--muted);
    white-space: nowrap;
  }
  .contact-line {
    position: absolute;
    top: 198px;
    left: 0;
    width: 100%;
    text-align: center;
    font-family: "Open Sans", sans-serif;
    font-weight: 300;
    font-size: 9px;
    color: var(--muted);
  }
</style>
</head>
<body>
  <main class="canvas">
    <section class="card-face card-front">
      <div class="monogram-disc">
        <span class="monogram-name">Rosalind<br>Pember</span>
      </div>
    </section>
    <section class="card-face card-back">
      <h1 class="holder-name">Rosalind Pember</h1>
      <div class="role-line">
        <span class="rule"></span>
        <span class="role-title">STYLIST OR WARDROBE STYLIST</span>
        <span class="rule"></span>
      </div>
      <p class="contact-line">rosapember@quillnet.co.nz | 0218846193</p>
    </section>
  </main>
</body>
</html>
```